Solace Chiropractic & Acupuncture Business Cards

I need a business card design that feels elevated. I am open to any of the logo designs uploaded. We have two doctors so I'll need to be able to change out the names.

Information:
Marnie Toller D.C., Dipl. Ac. ASA
584 W 12th St, Ste 320
Fernvale, CO 67419
solacegrove.net
620-555-0147
drmarnie@solacegrove.com
Updates

We have designs we like now, we are just trying to choose between top contenders. Thanks for your submissions!

Contact Information for Business Card

noted in description

Requirements
Must have
• ability to edit info if possible
Nice to have
• Please see our website solacegrove.net for our style and colors

```html
<!DOCTYPE html>
<html lang="en">
<head>
<meta charset="utf-8">
<title>Solace Chiropractic &amp; Acupuncture — Business Cards</title>
<link rel="stylesheet" href="https://fonts.googleapis.com/css2?family=Cormorant+Garamond:wght@500&family=Lato:wght@400&display=swap">
<style>
  :root {
    --backdrop: #3b3b3d;
    --navy: #353c4f;
    --sand: #cdc4b9;
    --cream: #f4f3ec;
    --paper: #ffffff;
    --serif: "Cormorant Garamond", Georgia, serif;
    --sans: "Lato", Arial, sans-serif;
  }
  * { box-sizing: border-box; margin: 0; padding: 0; }
  html, body { width: 1200px; height: 900px; overflow: hidden; }
  body { background: var(--backdrop); position: relative; font-family: var(--sans); color: var(--navy); }

  .card { position: absolute; width: 514px; height: 296px; background: var(--paper); overflow: hidden; }
  .card--front { left: 73px; top: 138px; background: var(--cream); }
  .card--contact-split { left: 615px; top: 138px; }
  .card--badge { left: 73px; top: 465px; }
  .card--contact-panel { left: 615px; top: 465px; }

  .wordmark { font-family: var(--serif); font-weight: 500; color: var(--navy); line-height: 1; }
  .tagline { font-family: var(--serif); font-weight: 500; color: var(--navy); text-transform: uppercase; letter-spacing: 0.02em; }

  /* Front */
  .card--front .brand { position: absolute; left: 0; right: 0; top: 102px; text-align: center; }
  .card--front .wordmark { font-size: 82px; }
  .card--front .tagline { font-size: 13px; margin-top: 4px; }

  /* Contact, split layout */
  .card--contact-split .brand {
    position: absolute; left: 40px; top: 0; width: 180px; height: 296px;
    display: flex; flex-direction: column; align-items: center; justify-content: center; text-align: center;
  }
  .card--contact-split .brand-dot { width: 54px; height: 54px; border-radius: 50%; border: 1px solid var(--navy); margin-bottom: 14px; }
  .card--contact-split .wordmark { font-size: 40px; }
  .card--contact-split .tagline { font-size: 13px; line-height: 1.1; margin-top: 6px; }
  .card--contact-split .divider { position: absolute; left: 234px; top: 33px; width: 1px; height: 240px; background: var(--navy); }
  .card--contact-split .details { position: absolute; left: 269px; top: 72px; font-size: 14px; line-height: 1.35; }
  .card--contact-split .details .address { font-size: 13px; }

  .details .name { margin-bottom: 18px; }
  .details .lines { margin-bottom: 12px; }

  /* Badge */
  .card--badge .badge {
    position: absolute; left: 170px; top: 38px; width: 172px; height: 222px; border-radius: 50%;
    background: var(--sand); box-shadow: 0 0 0 4px var(--paper), 0 0 0 5px var(--sand);
    display: flex; align-items: center; justify-content: center;
  }
  .card--badge .wordmark { font-size: 40px; color: var(--cream); }

  /* Contact, panel layout */
  .card--contact-panel .brand { position: absolute; left: 48px; top: 32px; }
  .card--contact-panel .wordmark { font-size: 42px; }
  .card--contact-panel .tagline { font-size: 7px; margin-top: 2px; }
  .card--contact-panel .details { position: absolute; left: 48px; top: 122px; font-size: 14px; line-height: 1.3; letter-spacing: 0.02em; }
  .card--contact-panel .details .name { margin-bottom: 30px; }
  .card--contact-panel .details .lines { margin-bottom: 8px; }
  .card--contact-panel .panel {
    position: absolute; left: 285px; top: 0; width: 229px; height: 296px;
    background: linear-gradient(135deg, var(--sand) 0%, var(--sand) 58%, var(--navy) 58%, var(--navy) 64%, var(--sand) 64%);
  }
</style>
</head>
<body>

  <section class="card card--front">
    <div class="brand">
      <div class="wordmark">Solace</div>
      <div class="tagline">Chiropractic &amp; Acupuncture</div>
    </div>
  </section>

  <section class="card card--contact-split">
    <div class="brand">
      <div class="brand-dot"></div>
      <div class="wordmark">Solace</div>
      <div class="tagline">Chiropractic<br>&amp; Acupuncture</div>
    </div>
    <div class="divider"></div>
    <div class="details">
      <p class="name">Marnie Toller D.C., Dipl. Ac. ASA</p>
      <p class="lines">620-555-0147<br>drmarnie@solacegrove.com</p>
      <p class="lines address">584 W 12th St, Ste 320<br>Fernvale, CO 67419</p>
      <p>solacegrove.net</p>
    </div>
  </section>

  <section class="card card--badge">
    <div class="badge">
      <div class="wordmark">Solace</div>
    </div>
  </section>

  <section class="card card--contact-panel">
    <div class="brand">
      <div class="wordmark">Solace</div>
      <div class="tagline">Chiropractic &amp; Acupuncture</div>
    </div>
    <div class="details">
      <p class="name">Marnie Toller D.C., Dipl. Ac. ASA</p>
      <p class="lines">620-555-0147<br>drmarnie@solacegrove.com</p>
      <p class="lines">584 W 12th St, Ste 320<br>Fernvale, CO 67419</p>
      <p>solacegrove.net</p>
    </div>
    <div class="panel" role="img" aria-label="Large decorative brand initial on a sand-coloured panel"></div>
  </section>

</body>
</html>
```